依頼概要
■依頼の目的/概要
薬局で作っているかぜ薬の販促用のポスターを作成して頂きたいです。

■依頼詳細
以下の4つの文言と当社の社長の写真を入れたポスターのデザインをお願いします。

・私が毎日心を込めて作っております(キャッチコピー)
・薬剤師手作りのかぜ薬(キャッチコピーの下に一回り小さい文字でいれる)
・一度飲んだら手放せなくなります
・特に仕事で忙しくて病院に行けない方はご家庭に必携です
・社長の写真

薬局内に掲示するポスターになります。
実際に掲示するポスターのサイズはA0サイズで考えていますが、デザインはA4サイズでの作成をお願いいたします。
※社長の写真は添付ファイルにてご確認ください。

その他何かご不明な点がございましたら、お気軽にご質問下さい。
よろしくお願いいたします。
ポスター内の文字に関して、縦書きなら縦書き、横書きなら横書きに統一をお願いいたします。

仕事で忙しい方にも目にとまるようなデザインだったので、選ばせていただきました。

提案していただいたランサーの皆さん、ありがとうございました。

```html
<!DOCTYPE html>
<html lang="ja">
<head>
<meta charset="UTF-8">
<title>薬剤師手作りのかぜ薬</title>
<link rel="stylesheet" href="https://fonts.googleapis.com/css2?family=Noto+Serif+JP:wght@500;600;700&family=Noto+Sans+JP:wght@500&display=swap">
<style>
  :root {
    --sage: #d5e2d1;
    --paper: #ffffff;
    --ink: #2b2b2b;
    --accent: #c8434b;
    --glass: #f4f8f2;
    --photo-a: #c9d4dd;
    --photo-b: #8e9ca8;
  }
  * { margin: 0; padding: 0; box-sizing: border-box; }
  html, body { width: 846px; height: 1200px; overflow: hidden; }
  body { background: var(--sage); font-family: "Noto Serif JP", serif; color: var(--ink); }
  .poster { position: relative; width: 846px; height: 1200px; background: var(--sage); }

  .headline-panel {
    position: absolute; left: 0; top: 28px; width: 846px; height: 400px;
    background: var(--paper);
    display: flex; flex-direction: column; align-items: center; justify-content: center;
  }
  .headline {
    font-weight: 600; font-size: 62px; line-height: 1.38; letter-spacing: 0.04em; text-align: center;
  }
  .headline span { display: block; }
  .heart-mark {
    display: inline-flex; align-items: center; justify-content: center;
    width: 86px; height: 86px; border-radius: 50%;
    background: var(--accent); color: var(--paper);
    margin: 4px 2px 4px 0; vertical-align: middle;
  }

  .subhead {
    position: absolute; left: 0; top: 495px; width: 846px; text-align: center;
    font-weight: 600; letter-spacing: 0.05em;
  }
  .subhead .lead { font-size: 38px; }
  .subhead .product { font-size: 50px; margin-left: 14px; }

  .portrait {
    position: absolute; left: 287px; top: 556px; width: 272px; height: 272px; border-radius: 50%;
    border: 6px solid var(--paper);
    background: radial-gradient(circle at 45% 40%, var(--photo-a), var(--photo-b));
  }

  .glassware {
    position: absolute; left: 96px; top: 850px; width: 540px; height: 108px;
    background: var(--glass); opacity: 0.8; border-radius: 6px;
  }
  .divider { position: absolute; left: 654px; top: 845px; width: 3px; height: 118px; background: var(--paper); }

  .body-copy {
    position: absolute; left: 0; top: 1058px; width: 846px; text-align: center;
    font-family: "Noto Sans JP", sans-serif; font-weight: 500; font-size: 25px; line-height: 1.55;
  }
</style>
</head>
<body>
<main class="poster">
  <section class="headline-panel">
    <h1 class="headline">
      <span>私が毎日</span>
      <span><b class="heart-mark">心</b>を込めて</span>
      <span>作っております</span>
    </h1>
  </section>

  <p class="subhead"><span class="lead">薬剤師手作りの</span><span class="product">かぜ薬</span></p>

  <div class="portrait" role="img" aria-label="薬を調合する薬剤師の写真"></div>

  <div class="glassware" role="img" aria-label="フラスコやビーカーなど実験器具のイラスト"></div>
  <div class="divider"></div>

  <p class="body-copy">
    一度飲んだら手放せなくなります<br>
    特に仕事で忙しくて病院に行けない方はご家庭に必携です
  </p>
</main>
</body>
</html>
```